Cooking oil

To design a label for palm cooking oil (16,1x15,1cm). The brand is Tumbra (logo enclosed). 20lit plastic container. The container colour is yellow and the cap colour is red.
Label background colour yellow.
Attached are examples to give an idea.

```html
<!DOCTYPE html>
<html lang="en">
<head>
<meta charset="utf-8">
<title>Tumbra Palm Olein Label</title>
<link rel="stylesheet" href="https://fonts.googleapis.com/css2?family=Oswald:wght@500;600;700&family=Raleway:wght@200&family=Sacramento&display=swap">
<style>
  :root {
    --yellow-light: #ffe14a;
    --yellow: #fbd20a;
    --yellow-deep: #f4b400;
    --orange: #f08a0c;
    --red: #e01f26;
    --white: #ffffff;
  }
  html, body {
    margin: 0;
    padding: 0;
    width: 1200px;
    height: 3170px;
    overflow: hidden;
    background: var(--white);
  }
  .label {
    position: relative;
    width: 1200px;
    height: 3170px;
  }
  .label-shape {
    position: absolute;
    inset: 0;
  }
  .brand {
    position: absolute;
    left: 0;
    width: 1200px;
    top: 520px;
    text-align: center;
    font-family: "Oswald", sans-serif;
    font-weight: 700;
    font-size: 110px;
    color: var(--red);
    letter-spacing: 2px;
    line-height: 1;
  }
  .title-script {
    position: absolute;
    left: 0;
    width: 1200px;
    text-align: center;
    font-family: "Sacramento", cursive;
    color: var(--white);
    text-shadow: 0 0 10px rgba(255,255,255,0.9), 0 0 24px rgba(255,255,255,0.6);
    line-height: 1;
  }
  .title-palm {
    top: 920px;
    font-size: 400px;
  }
  .title-olein {
    position: absolute;
    left: 0;
    width: 1200px;
    top: 1280px;
    text-align: center;
    font-family: "Raleway", sans-serif;
    font-weight: 200;
    font-size: 290px;
    line-height: 1;
    color: var(--white);
    letter-spacing: -6px;
  }
  .divider {
    position: absolute;
    left: 598px;
    top: 1608px;
    width: 4px;
    height: 325px;
    background: var(--white);
  }
  .title-pure {
    top: 1940px;
    font-size: 260px;
  }
  .nutrition {
    position: absolute;
    left: 387px;
    top: 2290px;
    width: 430px;
    color: var(--white);
    font-family: "Oswald", sans-serif;
  }
  .nutrition-heading {
    margin: 0 0 42px;
    font-weight: 600;
    font-size: 64px;
    line-height: 1;
    letter-spacing: -1px;
    white-space: nowrap;
    transform: scaleX(0.78);
    transform-origin: left;
    width: 550px;
  }
  .nutrition-table {
    width: 100%;
    border-collapse: collapse;
    font-weight: 600;
    font-size: 34px;
    line-height: 50px;
  }
  .nutrition-table td { padding: 0; }
  .nutrition-table td.amount { text-align: right; }
  .volume {
    position: absolute;
    left: 0;
    width: 1200px;
    top: 2912px;
    text-align: center;
    font-family: "Oswald", sans-serif;
    font-weight: 600;
    font-size: 62px;
    line-height: 1;
    color: var(--white);
  }
</style>
</head>
<body>
<main class="label">
  <svg class="label-shape" width="1200" height="3170" viewBox="0 0 1200 3170" xmlns="http://www.w3.org/2000/svg">
    <defs>
      <linearGradient id="label-fill" x1="0" y1="0" x2="1" y2="1">
        <stop offset="0" stop-color="#f6b800"/>
        <stop offset="0.45" stop-color="#fcd40c"/>
        <stop offset="0.75" stop-color="#fbcd06"/>
        <stop offset="1" stop-color="#f3b100"/>
      </linearGradient>
      <linearGradient id="leaf-tone" x1="0" y1="0" x2="1" y2="1">
        <stop offset="0" stop-color="#f08a0c" stop-opacity="0.75"/>
        <stop offset="1" stop-color="#f6b400" stop-opacity="0"/>
      </linearGradient>
      <radialGradient id="fruit-left" cx="0.3" cy="0.5" r="0.6">
        <stop offset="0" stop-color="#f07a10"/>
        <stop offset="1" stop-color="#f4a800" stop-opacity="0"/>
      </radialGradient>
      <radialGradient id="fruit-right" cx="0.6" cy="0.5" r="0.6">
        <stop offset="0" stop-color="#f5b000"/>
        <stop offset="1" stop-color="#fbd20a" stop-opacity="0"/>
      </radialGradient>
      <clipPath id="label-clip">
        <polygon points="600,0 1200,167 1200,3000 600,3170 0,3000 0,167"/>
      </clipPath>
    </defs>

    <polygon class="label-body" points="600,0 1200,167 1200,3000 600,3170 0,3000 0,167" fill="url(#label-fill)"/>

    <g clip-path="url(#label-clip)">
      <rect role="img" aria-label="Palm frond illustration" x="0" y="580" width="780" height="1500" fill="url(#leaf-tone)"/>
      <rect role="img" aria-label="Cut palm fruit photograph" x="0" y="2480" width="360" height="650" fill="url(#fruit-left)"/>
      <rect role="img" aria-label="Whole palm fruit photograph" x="820" y="2600" width="380" height="500" fill="url(#fruit-right)"/>
    </g>

    <polygon class="inner-frame" points="600,75 1133,233 1133,2933 600,3075 67,2933 67,233" fill="none" stroke="#ffffff" stroke-width="10"/>

    <path class="logo-drop" d="M600,117 C680,230 890,360 890,500 C890,660 760,783 600,783 C440,783 310,660 310,500 C310,360 520,230 600,117 Z" fill="#ffffff"/>
  </svg>

  <div class="brand">Tumbra</div>

  <div class="title-script title-palm">Palm</div>
  <div class="title-olein">OLEIN</div>
  <div class="divider"></div>
  <div class="title-script title-pure">Pure</div>

  <section class="nutrition">
    <h2 class="nutrition-heading">NUTRITIONAL VALUES</h2>
    <table class="nutrition-table">
      <tr><td>Energy</td><td class="amount">900 kcal</td></tr>
      <tr><td>Protein</td><td class="amount">0 gm</td></tr>
      <tr><td>Total fat</td><td class="amount">100 gm</td></tr>
      <tr><td>Vitamin A</td><td class="amount">750 mcg</td></tr>
      <tr><td>Vitamin D</td><td class="amount">10 mcg</td></tr>
      <tr><td>Trans fats</td><td class="amount">&lt; 2 gm</td></tr>
      <tr><td>Cholestrol</td><td class="amount">0 mg</td></tr>
      <tr><td>Saturated fats</td><td class="amount">&lt; 17 gm</td></tr>
    </table>
  </section>

  <div class="volume">500 ML</div>
</main>
</body>
</html>
```